Marrowfield Contracting Business Cards

Front of card:

Full Logo
Name
Address
Office Phone
Cell Phone
Email
Website

Back:
Logo Mark in background
List and markets and services performed

```html
<!DOCTYPE html>
<html lang="en">
<head>
<meta charset="utf-8">
<title>Marrowfield Contracting Business Cards</title>
<link href="https://fonts.googleapis.com/css2?family=Montserrat:wght@400;500;700&family=Roboto+Slab:wght@300;400&display=swap" rel="stylesheet">
<style>
  :root {
    --stage: #3a3a3a;
    --red: #d62328;
    --grey: #7a7a7a;
    --ink: #1e1e1e;
    --white: #ffffff;
  }
  * { box-sizing: border-box; margin: 0; padding: 0; }
  html, body { width: 1200px; height: 689px; overflow: hidden; }
  body { background: var(--stage); position: relative; font-family: "Montserrat", sans-serif; }

  .card {
    position: absolute; top: 196px; width: 520px; height: 297px;
    overflow: hidden; background: var(--white);
  }
  .card--back { left: 50px; }
  .card--front { left: 630px; background: var(--red); }
  .card__shapes { position: absolute; inset: 0; width: 100%; height: 100%; }

  .wordmark { position: absolute; display: flex; align-items: center; gap: 12px; }
  .wordmark__dot { width: 46px; height: 46px; border-radius: 50%; background: var(--grey); flex: none; }
  .wordmark__name {
    color: var(--red); font-weight: 700; text-transform: uppercase;
    line-height: 1.05; letter-spacing: 0.06em;
  }
  .card--back .wordmark { left: 110px; top: 100px; }
  .card--back .wordmark__name { font-size: 27px; }
  .card--front .wordmark { left: 322px; top: 98px; flex-direction: column; align-items: flex-start; gap: 10px; }
  .card--front .wordmark__dot { width: 40px; height: 40px; }
  .card--front .wordmark__name { font-size: 18px; }

  .tagline {
    position: absolute; left: 0; right: 0; top: 196px; text-align: center;
    font-size: 12px; font-weight: 500; color: var(--ink); letter-spacing: 0.02em;
  }

  .contact { position: absolute; left: 26px; top: 58px; color: var(--white); }
  .contact__name { font-size: 19px; font-weight: 700; letter-spacing: 0.04em; margin-left: 48px; }
  .contact__role { font-size: 14px; font-weight: 400; margin: 2px 0 0 60px; }
  .contact__lines {
    position: absolute; top: 80px; left: 70px; width: 220px;
    font-family: "Roboto Slab", serif; font-weight: 300; font-size: 11.5px; line-height: 1.35;
  }
  .contact__group { height: 46px; }
</style>
</head>
<body>

  <section class="card card--back" aria-label="Card back">
    <svg class="card__shapes" viewBox="0 0 520 297" aria-hidden="true">
      <polygon points="345,0 520,0 520,44" fill="var(--red)"/>
      <polygon points="330,0 342,0 520,48 520,58" fill="var(--grey)"/>
      <polygon points="0,253 175,297 0,297" fill="var(--red)"/>
      <polygon points="0,239 190,297 178,297 0,249" fill="var(--grey)"/>
    </svg>
    <div class="wordmark">
      <span class="wordmark__dot"></span>
      <span class="wordmark__name">Marrowfield<br>Contracting</span>
    </div>
    <p class="tagline">List and markets and services performed</p>
  </section>

  <section class="card card--front" aria-label="Card front">
    <svg class="card__shapes" viewBox="0 0 520 297" aria-hidden="true">
      <polygon points="262,0 292,0 288,72" fill="var(--grey)"/>
      <polygon points="392,297 448,297 416,252" fill="var(--grey)"/>
      <polygon points="294,0 520,0 520,297 460,297 300,226 296,72" fill="var(--white)"/>
      <polygon points="300,0 310,0 314,212 462,280 462,288 306,219" fill="var(--red)"/>
      <polyline points="284,78 288,214 420,270" fill="none" stroke="var(--white)" stroke-width="4"/>

      <line x1="44" y1="95" x2="44" y2="262" stroke="var(--white)" stroke-width="2"/>
      <g fill="var(--red)" stroke="var(--white)" stroke-width="3">
        <polygon points="44,79 58,87 58,103 44,111 30,103 30,87" fill="var(--white)" stroke="none"/>
        <polygon points="44,129 58,137 58,153 44,161 30,153 30,137"/>
        <polygon points="44,180 58,188 58,204 44,212 30,204 30,188"/>
        <polygon points="44,231 58,239 58,255 44,263 30,255 30,239"/>
      </g>
      <circle cx="44" cy="91" r="4" fill="var(--red)"/>
      <path d="M36 102 q8 -10 16 0 z" fill="var(--red)"/>
      <path d="M37 148 h14 v4 h-14 z M39 144 h10 l2 4 h-14 z" fill="var(--white)"/>
      <circle cx="44" cy="196" r="7" fill="none" stroke="var(--white)" stroke-width="1.5"/>
      <path d="M37 196 h14 M44 189 v14 M40 190 q-3 6 0 12 M48 190 q3 6 0 12" fill="none" stroke="var(--white)" stroke-width="1"/>
      <path d="M44 256 l-6 -8 a6 6 0 1 1 12 0 z" fill="var(--white)"/>
      <circle cx="44" cy="246" r="2.2" fill="var(--red)"/>
    </svg>

    <div class="contact">
      <p class="contact__name">OWEN TALLIS</p>
      <p class="contact__role">Founder</p>
      <div class="contact__lines">
        <div class="contact__group">555 0142 3801<br>555 0142 3802</div>
        <div class="contact__group">hello@marrowfieldco.com<br>www.marrowfieldco.com</div>
        <div class="contact__group">27, 2nd Floor,<br>Elm Row, NY 104520</div>
      </div>
    </div>

    <div class="wordmark">
      <span class="wordmark__dot"></span>
      <span class="wordmark__name">Marrowfield<br>Contracting</span>
    </div>
  </section>

</body>
</html>
```